Business Card Design

I used to run a Mountaineering school and am getting back into business and just want a generic type card with an adventure theme. Core activities will be mountaineering, rock climbing, canyoning, expeditions, cross country skiing,

Industry/Entity Type

School

Contact Information for Business Card

Colin Ashby Adventure Guide
email: tallpinecolin@mailvane.net
+61472 836 915.

```html
<!DOCTYPE html>
<html lang="en">
<head>
<meta charset="utf-8">
<title>Colin Ashby – Adventure Guide</title>
<link rel="stylesheet" href="https://fonts.googleapis.com/css2?family=Saira+Stencil+One&family=Montserrat:wght@600&display=swap">
<style>
  :root {
    --sky: #4f5f5f;
    --haze: #8e9f9c;
    --cloud: #c9d3d0;
    --snow: #e3e9e7;
    --rock: #34423f;
    --rock-deep: #1f2928;
    --ink-light: #f4f6f5;
    --emblem-fill: rgba(244, 246, 245, 0.85);
  }
  html, body {
    margin: 0;
    padding: 0;
    width: 1200px;
    height: 741px;
    overflow: hidden;
    background: var(--rock);
  }
  .card {
    position: relative;
    width: 1200px;
    height: 741px;
    overflow: hidden;
  }
  .card__scenery {
    position: absolute;
    inset: 0;
    background:
      radial-gradient(ellipse 22% 12% at 40% 96%, rgba(227,233,231,0.95), transparent 75%),
      radial-gradient(ellipse 18% 30% at 50% 88%, rgba(227,233,231,0.7), transparent 75%),
      radial-gradient(ellipse 35% 40% at 88% 62%, rgba(214,223,220,0.9), transparent 72%),
      radial-gradient(ellipse 20% 22% at 98% 30%, rgba(201,211,208,0.6), transparent 75%),
      radial-gradient(ellipse 14% 26% at 54% 22%, rgba(31,41,40,0.85), transparent 72%),
      radial-gradient(ellipse 16% 20% at 40% 28%, rgba(52,66,63,0.8), transparent 72%),
      radial-gradient(ellipse 18% 30% at 8% 40%, rgba(52,66,63,0.75), transparent 72%),
      radial-gradient(ellipse 22% 22% at 18% 68%, rgba(31,41,40,0.55), transparent 72%),
      radial-gradient(ellipse 40% 14% at 25% 12%, rgba(201,211,208,0.55), transparent 75%),
      radial-gradient(ellipse 30% 10% at 80% 20%, rgba(201,211,208,0.5), transparent 75%),
      linear-gradient(180deg, var(--sky) 0%, var(--haze) 18%, #6d7d7b 40%, #8a9a97 65%, var(--cloud) 100%);
  }
  .card__content {
    position: absolute;
    inset: 0;
    color: var(--ink-light);
    text-align: center;
  }
  .card__emblem {
    position: absolute;
    left: 570px;
    top: 172px;
    width: 60px;
    height: 50px;
    background: var(--emblem-fill);
    border-radius: 4px;
  }
  .card__name {
    position: absolute;
    left: 0;
    right: 0;
    top: 248px;
    margin: 0;
    font-family: "Saira Stencil One", sans-serif;
    font-weight: 400;
    font-size: 110px;
    line-height: 1;
    letter-spacing: 10px;
    text-transform: uppercase;
  }
  .card__role {
    position: absolute;
    left: 0;
    right: 0;
    top: 366px;
    margin: 0;
    font-family: "Saira Stencil One", sans-serif;
    font-weight: 400;
    font-size: 70px;
    line-height: 1;
    letter-spacing: 6px;
    text-transform: uppercase;
    display: flex;
    justify-content: center;
    align-items: center;
    gap: 20px;
  }
  .card__role-dot {
    width: 9px;
    height: 9px;
    border-radius: 50%;
    background: var(--ink-light);
  }
  .card__contact {
    position: absolute;
    left: 0;
    right: 0;
    top: 655px;
    margin: 0;
    font-family: "Montserrat", sans-serif;
    font-weight: 600;
    font-size: 28px;
    line-height: 34px;
    letter-spacing: 2px;
    text-transform: uppercase;
  }
</style>
</head>
<body>
  <main class="card">
    <div class="card__scenery" role="img" aria-label="Monochrome photograph of a climber walking along a snowy ridge towards a high mountain peak above the clouds"></div>
    <div class="card__content">
      <div class="card__emblem" role="img" aria-label="Crossed ice axes emblem"></div>
      <h1 class="card__name">Colin Ashby</h1>
      <p class="card__role"><span class="card__role-dot"></span>Adventure Guide<span class="card__role-dot"></span></p>
      <p class="card__contact">tallpinecolin@mailvane.net | +61472 836 915</p>
    </div>
  </main>
</body>
</html>
```